Start-up company developing economical and ecological hydrogen peroxide generator needs an attractiv

We need a powerpoint design for a start-up company based in Montreal called Vorbelle currently seeking to raise funds from investors. We develop an electrochemical hydrogen peroxide generator based on new generation catalysts.

These generators allow industrial users of hydrogen peroxide to generate it onsite economically and ecologically, as opposed to buying it from the major suppliers who make it large production plants using more polluting methods and need to transport it to customers over long distances.

We would like to see designs that have a cleantech technology and green chemistry feel. Colors that evoke a sense of environmental sustainability are desired.

The final design should communicate technological innovation that makes the world a cleaner and healthier place to live.

Target Market(s)

Industrial users or producers of of hydrogen peroxide

Industry/Entity Type

It Company

Font styles to use
Sans Serif

Colors
0255a3
3276b5
85acd3
9bcb3b
add136
e3eebf

Requirements
Must have
• Clean, attractive, professional and advanced technology look.
• Our slogan is: Catalyst for innovation
Nice to have
• The cover page should have our logo and our slogan. It should also have some graphics that pertain to technology and green chemistry. The perception that one should have when looking at it is that the company is developing a clean chemical manufacturing technology that is more environmentally friendly.
• Each other template page should have our logo discretely included in it.
• Other than the cover page, the template pages should not be too crowded with design elements. There should be lots of clear space to add material.
• I have uploaded some inspirational images that can be used to help come up with some designs.

```html
<!DOCTYPE html>
<html lang="en">
<head>
<meta charset="UTF-8">
<title>Vorbelle – Title Slide</title>
<link href="https://fonts.googleapis.com/css2?family=Roboto:wght@300;400;700&family=Roboto+Condensed:wght@700&display=swap" rel="stylesheet">
<style>
  :root {
    --ink-dark: #333333;
    --brand-blue: #0d3d8f;
    --accent-blue: #0255a3;
    --mid-blue: #3276b5;
    --soft-blue: #85acd3;
    --leaf-green: #9bcb3b;
    --lime-green: #add136;
    --mist-green: #e3eebf;
    --body-grey: #555555;
    --band-start: #0a3a8c;
    --band-end: #3c62a3;
    --paper: #ffffff;
  }
  * { margin: 0; padding: 0; box-sizing: border-box; }
  html, body {
    width: 1200px;
    height: 900px;
    overflow: hidden;
    background: var(--paper);
  }
  .slide {
    position: relative;
    width: 1200px;
    height: 900px;
    overflow: hidden;
    background: var(--paper);
    font-family: "Roboto", Arial, sans-serif;
  }
  .cleantech-arcs {
    position: absolute;
    top: 0;
    right: 0;
    width: 420px;
    height: 320px;
  }
  .brand {
    position: absolute;
    top: 362px;
    left: 0;
    width: 100%;
    display: flex;
    justify-content: center;
    align-items: center;
    gap: 18px;
  }
  .brand-dot {
    width: 22px;
    height: 22px;
    border-radius: 50%;
    background: var(--accent-blue);
  }
  .brand-name {
    font-weight: 400;
    font-size: 84px;
    line-height: 1;
    letter-spacing: 1px;
    color: var(--ink-dark);
  }
  .brand-slogan {
    position: absolute;
    top: 468px;
    left: 0;
    width: 100%;
    text-align: center;
    font-weight: 400;
    font-size: 22px;
    letter-spacing: 3px;
    text-transform: uppercase;
    color: var(--leaf-green);
  }
  .slide-title {
    position: absolute;
    top: 574px;
    left: 0;
    width: 100%;
    text-align: center;
    font-family: "Roboto Condensed", "Arial Narrow", sans-serif;
    font-weight: 700;
    font-size: 52px;
    line-height: 1.2;
    color: var(--brand-blue);
  }
  .slide-subtitle {
    position: absolute;
    top: 650px;
    left: 0;
    width: 100%;
    text-align: center;
    font-weight: 300;
    font-size: 24px;
    line-height: 37.5px;
    color: var(--body-grey);
  }
  .slide-subtitle span { display: block; }
  .green-rule {
    position: absolute;
    left: 0;
    bottom: 36px;
    width: 100%;
    height: 6px;
    background: linear-gradient(90deg, var(--leaf-green), var(--lime-green), var(--mist-green));
  }
  .footer-band {
    position: absolute;
    left: 0;
    bottom: 0;
    width: 100%;
    height: 36px;
    background: linear-gradient(90deg, var(--band-start), var(--band-end));
    display: flex;
    align-items: center;
  }
  .page-number {
    margin-left: 14px;
    color: var(--paper);
    font-weight: 700;
    font-size: 18px;
  }
</style>
</head>
<body>
  <main class="slide">
    <svg class="cleantech-arcs" viewBox="0 0 420 320" aria-hidden="true">
      <circle cx="420" cy="0" r="300" fill="none" stroke="var(--mist-green)" stroke-width="2"/>
      <circle cx="420" cy="0" r="240" fill="none" stroke="var(--soft-blue)" stroke-width="1.5" opacity="0.5"/>
      <circle cx="420" cy="0" r="180" fill="none" stroke="var(--leaf-green)" stroke-width="1.5" opacity="0.45"/>
      <circle cx="420" cy="0" r="120" fill="var(--mist-green)" opacity="0.5"/>
    </svg>

    <div class="brand">
      <div class="brand-dot"></div>
      <div class="brand-name">Vorbelle</div>
    </div>
    <p class="brand-slogan">Catalyst for innovation</p>

    <h1 class="slide-title">Title Text Here</h1>

    <p class="slide-subtitle">
      <span>Subteaxt here Subteaxt here Subteaxt here Subteaxt</span>
      <span>here Subteaxt here Subteaxt here Subteaxt here Sub-</span>
      <span>teaxt here</span>
    </p>

    <div class="green-rule"></div>
    <footer class="footer-band">
      <span class="page-number">1</span>
    </footer>
  </main>
</body>
</html>
```